Design a Logo + Coming soon page for website

Need a logo design AND a coming soon page featuring this logo please.
Prefer sans-serif fonts for this.

-----------
Logo design:
Modern, bold, corporate logo with "QDM" on it. Want some options with bright colour and black/white/grey scale. This is a importer selling to distributors and wholesalers, not to the public; but we don't want it to be industry specific, so nothing too specific in iconography (circles, squares etc. are fine).
-----------
Coming soon page:
We will most likely be starting off with a cover page using sqaurespace (http://www.pagelarkhub.com/home/coverpages/). We need a logo and design to get started.
*Bold* coming soon page for website with large logo. CTA is to contact via email.

*Sample text* for coming soon page is as follows:
Brand new website for quality baking products coming soon.
Wholesalers, distributors in Sydney, Melbourne and Brisbane contact sales@qdm.com.au
-----------
** Note: Will be looking at designing entire website soon and this may be used as a basis, so looking forward to seeing what you've got! **

```html
<!DOCTYPE html>
<html lang="en">
<head>
<meta charset="utf-8">
<title>QDM – Coming soon</title>
<link rel="stylesheet" href="https://fonts.googleapis.com/css2?family=Carlito:wght@400;700&display=swap">
<style>
  :root {
    --page-bg: #ffffff;
    --heading-grey: #8a8a8a;
    --heading-shadow: #d9d9d9;
    --brand-grey: #6a6a6a;
    --body-grey: #6b6b6b;
    --divider-grey: #7a7a7a;
    --footer-grey: #555555;
  }
  html, body {
    margin: 0;
    padding: 0;
    width: 1200px;
    height: 900px;
    overflow: hidden;
    background: var(--page-bg);
  }
  .cover-page {
    position: relative;
    width: 1200px;
    height: 900px;
    font-family: "Carlito", "Calibri", sans-serif;
  }
  .cover-title {
    position: absolute;
    left: 0;
    width: 1190px;
    top: 152px;
    margin: 0;
    text-align: center;
    font-size: 76px;
    font-weight: 700;
    letter-spacing: -2px;
    color: var(--heading-grey);
    text-shadow: -6px 4px 3px var(--heading-shadow);
  }
  .brand-name {
    position: absolute;
    left: 248px;
    top: 410px;
    width: 230px;
    margin: 0;
    font-size: 104px;
    font-weight: 700;
    line-height: 1;
    letter-spacing: -2px;
    color: var(--brand-grey);
  }
  .divider {
    position: absolute;
    left: 517px;
    top: 355px;
    width: 2px;
    height: 287px;
    background: var(--divider-grey);
  }
  .cover-message {
    position: absolute;
    left: 600px;
    top: 450px;
    margin: 0;
    font-size: 21px;
    font-weight: 700;
    line-height: 31px;
    letter-spacing: -0.6px;
    color: var(--body-grey);
  }
  .cover-message a {
    color: inherit;
    text-decoration: none;
  }
  .cover-footer {
    position: absolute;
    right: 28px;
    bottom: 22px;
    margin: 0;
    font-size: 12px;
    font-weight: 700;
    letter-spacing: -0.4px;
    color: var(--footer-grey);
  }
</style>
</head>
<body>
  <main class="cover-page">
    <h1 class="cover-title">Coming soon . . .</h1>

    <p class="brand-name">QDM</p>

    <div class="divider" aria-hidden="true"></div>

    <p class="cover-message">
      Brand new website for quality baking products coming soon.<br>
      Wholesalers, distributors in Sydney, Melbourne and Brisbane<br>
      Contact : <a href="mailto:sales@qdm.com.au">sales@qdm.com.au</a>
    </p>

    <p class="cover-footer">@ 2015 QDM, all rights reserved</p>
  </main>
</body>
</html>
```